Stationary pack for BrightVane

BrightVane is a recently establish Solar brokerage company based in Australia. We have a number of sales staff who provide advice and guidance to both residential and commercial customers regarding solar systems (solar hot water and solar panels.)

In addition to our brokerage services we are also developing software for the solar industry, which will be used to automate the solar system install process. This system will be used by other companies in the solar industry including installers, wholesalers and government departments.

We are after a stationary pack that consists of the following: Business cards, compliments slip and letter head.

The EPS, AI, PNG etc files for the logo are attached.

For the business card:
The name and logo of the company need to be clearly visible. On the back of the business cards, we would like the logo. I am happy for you to split the image part of the logo from the text if you think it would look better a different way.

I would like the business cards to be easily readable with the following information on the front:
Name
(Please leave room for titles for the future – eg Sales Advisor.)
Mobile
Office
Email
Address
ABN

Letter heads:
I would prefer the address to be at the top

Compliments slips:
Only need to be one sided

Target Market(s)

BrightVane provides services to both residential and commercial customers. Our customers will be environmentally conscious.

Industry/Entity Type

Residential

Requirements
Must have
• Business cards must have the logo on the back.

```html
<!DOCTYPE html>
<html lang="en">
<head>
<meta charset="utf-8">
<title>BrightVane Letterhead</title>
<link rel="stylesheet" href="https://fonts.googleapis.com/css2?family=Nunito:wght@800&family=Arimo:wght@700&display=swap">
<style>
  :root {
    --paper: #ffffff;
    --sun-light: #ecfb52;
    --sun-mid: #f1e844;
    --sun-deep: #f4d437;
    --leaf: #7ce41b;
    --brand-green: #3db318;
    --sun-disc: #fbc81f;
    --ghost: #fdfcf1;
  }
  * { margin: 0; padding: 0; box-sizing: border-box; }
  html, body { width: 849px; height: 1200px; overflow: hidden; background: var(--paper); }
  .letterhead {
    position: relative;
    width: 849px;
    height: 1200px;
    background: var(--paper);
    overflow: hidden;
  }
  .top-band {
    position: absolute;
    left: 0; top: 0;
    width: 849px; height: 124px;
    background: linear-gradient(to bottom, var(--sun-light) 0%, var(--sun-mid) 55%, var(--sun-deep) 100%);
  }
  .address-line {
    position: absolute;
    left: 31px; top: 132px;
    font-family: "Arimo", Arial, sans-serif;
    font-weight: 700;
    font-size: 13.5px;
    letter-spacing: -0.3px;
    color: var(--leaf);
    white-space: nowrap;
  }
  .lower-band {
    position: absolute;
    left: 0; top: 151px;
    width: 514px; height: 32px;
    background: linear-gradient(to bottom, #fbf7b0 0%, var(--sun-mid) 35%, var(--sun-deep) 100%);
  }
  .brand {
    position: absolute;
    right: 10px; top: 122px;
    font-family: "Nunito", Arial, sans-serif;
    font-weight: 800;
    font-size: 56px;
    line-height: 1;
    color: var(--brand-green);
    letter-spacing: -1px;
  }
  .brand-dot {
    position: absolute;
    left: 640px; top: 22px;
    width: 72px; height: 72px;
    border-radius: 50%;
    background: var(--sun-disc);
  }
  .ghost-disc {
    position: absolute;
    left: 20px; top: 690px;
    width: 640px; height: 640px;
    border-radius: 50%;
    background: var(--ghost);
  }
</style>
</head>
<body>
  <div class="letterhead">
    <div class="ghost-disc"></div>
    <div class="top-band"></div>
    <div class="brand-dot"></div>
    <p class="address-line">Address: &lt;address goes here address goes here address goes here &gt;</p>
    <div class="lower-band"></div>
    <div class="brand">BrightVane</div>
  </div>
</body>
</html>
```